Ready to eat rice packaging design

We need packaging design for pre cooked rice of different types
1. Basmati Rice
2. Brown basmati Rice
3. Jasmine Rice
4. Lemon Rice
5. Rice Pilaf
6. Biryani Rice

Back of the package will have preparation write up and Nutrition chart.

The design should have both natural as well as modern feel to it.

Examples of packages available in market enclosed.

Target Market(s)

National Food and Grocery Stores in USA

Industry/Entity Type

Grocery Store

```html
<!DOCTYPE html>
<html lang="en">
<head>
<meta charset="utf-8">
<title>Ready to Eat Basmati Rice – Pouch Front</title>
<link href="https://fonts.googleapis.com/css2?family=Cinzel:wght@700&family=Berkshire+Swash&display=swap" rel="stylesheet">
<style>
  :root {
    --gold-light: #f1dcaa;
    --gold-mid: #ddbd7c;
    --gold-deep: #c89f55;
    --stripe-pale: #f7e9b8;
    --stripe-bright: #efd37a;
    --wheat: #d9b567;
    --wheat-shade: #b98c3c;
    --ring-red: #8e1f22;
    --ring-cream: #ecd6a0;
    --ring-green: #1e6b3c;
    --rice-white: #f4f2ec;
    --rice-shade: #d8d6cf;
    --ribbon-light: #f3e0a8;
    --ribbon-dark: #c9a25a;
    --title-red: #8b1e1e;
    --name-brown: #4a3422;
  }
  * { box-sizing: border-box; margin: 0; padding: 0; }
  html, body {
    width: 1200px;
    height: 1200px;
    overflow: hidden;
    background: #d9d9d9;
  }
  .package-front {
    position: relative;
    width: 1200px;
    height: 1200px;
    overflow: hidden;
    background: linear-gradient(180deg, var(--gold-light) 0%, var(--gold-mid) 55%, var(--gold-deep) 100%);
  }
  .stripe-band {
    position: absolute;
    top: 0;
    bottom: 0;
    width: 250px;
    background: repeating-linear-gradient(90deg,
      transparent 0 14px,
      var(--stripe-pale) 14px 20px,
      transparent 20px 30px,
      var(--stripe-bright) 30px 33px,
      transparent 33px 44px);
    opacity: 0.8;
  }
  .stripe-band--left { left: 0; }
  .stripe-band--right { right: 0; }
  .center-panel {
    position: absolute;
    top: 0;
    bottom: 0;
    left: 250px;
    right: 250px;
    background: linear-gradient(180deg, rgba(247,230,186,0.6), rgba(226,196,130,0.4));
  }
  .label-title {
    position: absolute;
    top: 130px;
    left: 0;
    width: 100%;
    text-align: center;
    font-family: "Cinzel", "Times New Roman", serif;
    font-weight: 700;
    font-size: 58px;
    letter-spacing: 1px;
    color: var(--title-red);
  }
  .emblem {
    position: absolute;
    left: 0;
    top: 0;
    width: 1200px;
    height: 1200px;
  }
  .product-name {
    position: absolute;
    top: 975px;
    left: 0;
    width: 100%;
    text-align: center;
    font-family: "Berkshire Swash", "Georgia", cursive;
    font-size: 86px;
    color: var(--name-brown);
  }
</style>
</head>
<body>
  <main class="package-front">
    <div class="stripe-band stripe-band--left"></div>
    <div class="stripe-band stripe-band--right"></div>
    <div class="center-panel"></div>

    <h1 class="label-title">READY TO EAT</h1>

    <svg class="emblem" viewBox="0 0 1200 1200" xmlns="http://www.w3.org/2000/svg">
      <defs>
        <radialGradient id="wreath-fill" cx="50%" cy="50%" r="50%">
          <stop offset="80%" stop-color="var(--wheat)" stop-opacity="0"/>
          <stop offset="86%" stop-color="var(--wheat)"/>
          <stop offset="100%" stop-color="var(--wheat-shade)" stop-opacity="0.6"/>
        </radialGradient>
        <radialGradient id="rice-fill" cx="50%" cy="45%" r="55%">
          <stop offset="0%" stop-color="var(--rice-white)"/>
          <stop offset="100%" stop-color="var(--rice-shade)"/>
        </radialGradient>
        <linearGradient id="ribbon-fill" x1="0" y1="0" x2="0" y2="1">
          <stop offset="0%" stop-color="var(--ribbon-light)"/>
          <stop offset="100%" stop-color="var(--ribbon-dark)"/>
        </linearGradient>
      </defs>

      <g class="wheat-wreath" role="img" aria-label="Golden wreath of wheat ears around the emblem">
        <circle cx="600" cy="590" r="400" fill="url(#wreath-fill)"/>
      </g>

      <g class="ornament-ring" role="img" aria-label="Red and cream ornamental scroll border ring">
        <circle cx="600" cy="560" r="320" fill="var(--ring-red)"/>
        <circle cx="600" cy="560" r="300" fill="var(--ring-cream)" opacity="0.55"/>
        <circle cx="600" cy="560" r="282" fill="var(--ring-red)"/>
      </g>

      <circle class="ring-accent" cx="600" cy="560" r="276" fill="var(--ring-green)"/>

      <g class="rice-photo" role="img" aria-label="Photo of fluffy basmati rice with peas and diced carrots">
        <circle cx="600" cy="560" r="266" fill="url(#rice-fill)"/>
      </g>

      <g class="banner-ribbon" role="img" aria-label="Curled golden ribbon banner">
        <path d="M300 720 Q360 690 430 705 L460 800 Q390 790 330 820 Q350 770 300 720 Z" fill="url(#ribbon-fill)"/>
        <path d="M900 720 Q840 690 770 705 L740 800 Q810 790 870 820 Q850 770 900 720 Z" fill="url(#ribbon-fill)"/>
        <path d="M420 700 Q600 800 780 700 L790 790 Q600 880 410 790 Z" fill="url(#ribbon-fill)" stroke="var(--wheat-shade)" stroke-width="2"/>
      </g>
    </svg>

    <p class="product-name">Basmati Rice</p>
  </main>
</body>
</html>
```